Flyer Design Project

Business is Calloway In Home Care

We are an Australian provider of In Home Care services.

We have a focus on quality care and a high standard of service.

We are non medical

We want to promote the health, happiness and independence of senior citizens by providing some help at home for general domestic duties (cleaning, bed linnen), personal care (showering, grooming) and meal preparation etc.

Target Market(s)

Seniors (70+) and the Children of seniors.

Industry/Entity Type

Business

Requirements
Must have
• Colour scheme from our website (www.callowayinhomecare.com.au) –

The uploaded Word doc contains the desired copy.

Leaflet will be a standard A4 size foldout with 6 panels, 3 on each side.

```html
<!DOCTYPE html>
<html lang="en">
<head>
<meta charset="utf-8">
<title>Calloway In Home Care – Flyer</title>
<link rel="stylesheet" href="https://fonts.googleapis.com/css2?family=Handlee&family=Open+Sans:wght@400;600&display=swap">
<style>
  :root {
    --sky: #dbe9f6;
    --sky-deep: #c6dcef;
    --paper: #fbfdff;
    --divider: #c9def0;
    --ink: #1f1f1f;
    --orange: #f6a21e;
    --orange-soft: #f9c46b;
    --photo-warm: #c9a27a;
    --photo-green: #a9cf6a;
  }
  * { box-sizing: border-box; margin: 0; padding: 0; }
  html, body { width: 1200px; height: 848px; overflow: hidden; background: #ffffff; }
  .flyer {
    position: relative; width: 1200px; height: 848px; overflow: hidden;
    background: var(--paper);
    font-family: "Open Sans", Arial, sans-serif; color: var(--ink);
  }
  .header-wave { position: absolute; left: 0; top: 0; width: 1200px; height: 170px; }
  .divider { position: absolute; top: 120px; width: 1px; height: 700px; background: var(--divider); }
  .divider--one { left: 400px; }
  .divider--two { left: 800px; }

  .panel-title {
    position: absolute; font-family: "Handlee", cursive; font-weight: 400;
    font-size: 31px; line-height: 36px; text-align: center; color: var(--ink);
  }
  .panel-title--about { left: 60px; top: 34px; width: 280px; }
  .panel-title--mission { left: 440px; top: 48px; width: 320px; }
  .panel-title--assess { left: 810px; top: 12px; width: 390px; }

  .about-list { position: absolute; left: 48px; top: 160px; width: 330px; list-style: none; font-size: 18.5px; line-height: 24px; }
  .about-list li { margin-bottom: 24px; }
  .about-list li::before { content: "•"; margin-right: 10px; }

  .photo { position: absolute; }
  .photo--kitchen {
    left: 0; top: 516px; width: 316px; height: 228px;
    background: linear-gradient(135deg, #8a7a5c 0%, #c7b9a0 40%, #dfe6ef 70%, #9fb0c8 100%);
    box-shadow: 4px 4px 10px rgba(0,0,0,0.35);
  }
  .photo--game {
    left: 465px; top: 368px; width: 290px; height: 190px;
    transform: rotate(-12deg);
    background: linear-gradient(160deg, #d8e2ce 0%, #b7c6b0 40%, #d6c3ae 70%, #8b4a3a 100%);
    border: 6px solid #ffffff;
    box-shadow: 4px 6px 12px rgba(0,0,0,0.35);
  }
  .photo--hands {
    left: 801px; top: 93px; width: 399px; height: 256px;
    background: linear-gradient(120deg, #ffffff 0%, #eef6e0 30%, var(--photo-warm) 55%, var(--photo-green) 100%);
  }

  .contact { position: absolute; left: 0; width: 400px; text-align: center; }
  .contact__phone { top: 756px; font-size: 25px; letter-spacing: 0.5px; }
  .contact__web { top: 788px; font-size: 18px; }

  .mission-lead { position: absolute; left: 420px; top: 176px; width: 360px; text-align: center; font-size: 18.5px; line-height: 25px; }
  .mission-close { position: absolute; left: 410px; top: 628px; width: 380px; text-align: center; font-size: 18.5px; line-height: 25px; }

  .assess-intro { position: absolute; left: 815px; top: 360px; width: 370px; text-align: center; font-size: 16.5px; line-height: 21px; }
  .assess-heading { position: absolute; left: 818px; top: 490px; font-size: 16.5px; }
  .assess-list { position: absolute; left: 818px; top: 510px; width: 370px; list-style: none; font-size: 16.5px; line-height: 20.5px; }
  .assess-list li { position: relative; padding-left: 22px; }
  .assess-list li::before { content: "•"; position: absolute; left: 2px; }
  .assess-close { position: absolute; left: 815px; top: 740px; width: 380px; text-align: center; font-size: 16.5px; line-height: 20.5px; }

  .footer-rule { position: absolute; left: 0; width: 1200px; background: var(--orange); }
  .footer-rule--thick { top: 822px; height: 5px; }
  .footer-rule--thin { top: 838px; height: 2px; background: var(--orange-soft); }
</style>
</head>
<body>
<main class="flyer">
  <svg class="header-wave" viewBox="0 0 1200 170" preserveAspectRatio="none" aria-hidden="true">
    <path d="M0 0 H1200 V95 C1100 100 1000 130 900 128 C820 126 780 110 700 118 C560 132 460 110 330 118 C200 126 120 150 0 140 Z" fill="var(--sky)"/>
    <path d="M0 140 C120 150 200 126 330 118 C460 110 560 132 700 118 C780 110 820 126 900 128" fill="none" stroke="var(--sky-deep)" stroke-width="2"/>
  </svg>

  <div class="divider divider--one"></div>
  <div class="divider divider--two"></div>

  <section class="panel panel--about">
    <h2 class="panel-title panel-title--about">About us...</h2>
    <ul class="about-list">
      <li>We provide person-centred care that maximizes our client’s ability to be independent.</li>
      <li>We aim to improve our client’s wellbeing, self-confidence and connections to their community.</li>
      <li>We work in partnership with the care recipient (and stakeholders) to design a care plan that meets and exceeds expectations.</li>
    </ul>
    <div class="photo photo--kitchen" role="img" aria-label="Photo of a carer helping a senior woman prepare food in a kitchen"></div>
    <p class="contact contact__phone">CALL 1300 552 417</p>
    <p class="contact contact__web">www.callowayinhomecare.com.au</p>
  </section>

  <section class="panel panel--mission">
    <h2 class="panel-title panel-title--mission">Our Mission ..</h2>
    <p class="mission-lead">... to provide quality care that supports<br>people who wish to live independently, in the secure and familiar surroundings of their own home.</p>
    <div class="photo photo--game" role="img" aria-label="Photo of a young carer playing backgammon with a senior man outdoors"></div>
    <p class="mission-close">We achieve our mission through the open partnerships we create, that are based on trust and communication, and that embrace the philosophy of person-centred care.</p>
  </section>

  <section class="panel panel--assess">
    <h2 class="panel-title panel-title--assess">Complimentary<br>in-home assessment</h2>
    <div class="photo photo--hands" role="img" aria-label="Photo of a carer’s hands gently holding an older person’s hand"></div>
    <p class="assess-intro">During our initial assessment we find out about everyone involved<br>– the care recipient, their family, advocates and any other stakeholders.</p>
    <p class="assess-heading">We do this by:</p>
    <ul class="assess-list">
      <li>Assessing the care recipient and their home environment so that we fully understand the care recipient’s needs.</li>
      <li>Getting to know the care recipients background and interests.</li>
      <li>Assessing the home from an OH&amp;S perspective to ensure the safety of our care recipient and for the caregiver.</li>
      <li>Matching the care recipients needs to our service matrix.</li>
    </ul>
    <p class="assess-close">In partnership with the care recipient<br>(who is at the centre of our service),<br>we prepare a service delivery and care plan.</p>
  </section>

  <div class="footer-rule footer-rule--thick"></div>
  <div class="footer-rule footer-rule--thin"></div>
</main>
</body>
</html>
```